real esate business card with company logo and name

we need a business card design for a real esate company

The company name is Walsh & Brody Pty Ltd, and we have our logo designed and will upload. We want classic or moden feel. Black or white background. looks more textured. Should include folowinginformations
Paul Walsh and Lucy Brody
Sales Agents & Onsite Manager
p: 07 5948 2063
F: 07 5948 2174
M:0461 857 239
3/42 Marlin Crescent, ELLEN GROVE QLD 4078

We want this business card looks professonal. Thank you in advance.

Industry/Entity Type

Real Estate Agent

Contact Information for Business Card

Paul Walsh and Lucy Brody
Onsite Manager & Sales Agents
p: 07 5948 2063
M:0461 857 239

Font styles to use
Serif

Colors
000000
fbfbfb
333333
959595

Requirements
Must have
• company logo and name, black or white back ground

```html
<!DOCTYPE html>
<html lang="en">
<head>
<meta charset="utf-8">
<title>Walsh &amp; Brody Pty Ltd — Business Card</title>
<link href="https://fonts.googleapis.com/css2?family=PT+Sans:wght@400;700&family=Montserrat:wght@500&display=swap" rel="stylesheet">
<style>
  :root {
    --backdrop: #2b2b2b;
    --paper: #fbfbfb;
    --band: #b3b3b3;
    --rule: #7a7a7a;
    --ink: #333333;
    --ink-strong: #1e1e1e;
    --mark: #959595;
    --back-card: #4d4d4d;
    --white: #ffffff;
  }
  * { margin: 0; padding: 0; box-sizing: border-box; }
  html, body { width: 1200px; height: 750px; overflow: hidden; }
  body {
    background: var(--backdrop);
    position: relative;
    font-family: "PT Sans", Arial, sans-serif;
    color: var(--ink);
  }
  .card {
    position: absolute;
    top: 228px;
    width: 461px;
    height: 262px;
    overflow: hidden;
  }
  .card--front { left: 124px; background: var(--paper); }
  .card--back { left: 618px; background: var(--back-card); }

  .brand {
    position: absolute;
    left: 0; right: 0;
    display: flex;
    flex-direction: column;
    align-items: center;
  }
  .brand__square { display: block; }
  .brand__name {
    font-family: "Montserrat", Arial, sans-serif;
    font-weight: 500;
    letter-spacing: 0.3px;
    white-space: nowrap;
  }
  .card--front .brand { top: 18px; }
  .card--front .brand__square { background: var(--mark); width: 86px; height: 86px; }
  .card--front .brand__name { color: #4a4a4a; font-size: 10px; margin-top: 22px; }
  .card--back .brand { top: 66px; }
  .card--back .brand__square { background: var(--white); width: 100px; height: 100px; }
  .card--back .brand__name { color: var(--white); font-size: 11px; margin-top: 20px; }

  .roofline { position: absolute; left: 0; top: 140px; width: 461px; height: 16px; }
  .band {
    position: absolute;
    left: 0; top: 154px;
    width: 461px; height: 108px;
    background: var(--band);
  }
  .people {
    position: absolute;
    top: 8px; left: 0; right: 0;
    text-align: center;
    font-size: 16px;
    font-weight: 700;
    color: var(--ink-strong);
  }
  .role {
    position: absolute;
    top: 29px; left: 27px; right: 27px;
    display: flex; align-items: center; gap: 5px;
    font-size: 12px;
    color: var(--ink-strong);
  }
  .role::before, .role::after { content: ""; flex: 1; height: 1px; background: var(--ink-strong); }
  .contacts {
    position: absolute;
    left: 27px; top: 45px;
    list-style: none;
    font-size: 10.5px;
    color: var(--ink-strong);
  }
  .contacts li { display: flex; align-items: center; height: 17.5px; }
  .contacts svg { width: 12px; height: 12px; margin-right: 6px; fill: var(--ink-strong); }
  .address {
    position: absolute;
    right: 27px; top: 47px;
    text-align: right;
    font-style: normal;
    font-size: 10.5px;
    line-height: 15px;
    color: var(--ink-strong);
  }
  .address .web { letter-spacing: 1.6px; }
</style>
</head>
<body>
  <section class="card card--front">
    <div class="brand">
      <span class="brand__square"></span>
      <span class="brand__name">WALSH &amp; BRODY PTY LTD.</span>
    </div>
    <svg class="roofline" viewBox="0 0 461 16">
      <polyline points="0,13 82,13 96,5 110,13 461,13" fill="none" stroke="#7a7a7a" stroke-width="3"/>
    </svg>
    <div class="band">
      <div class="people">Paul Walsh &amp; Lucy Brody</div>
      <div class="role">Sales Agents &amp; Onsite Manager</div>
      <ul class="contacts">
        <li><svg viewBox="0 0 24 24"><path d="M6.6 10.8a15.1 15.1 0 0 0 6.6 6.6l2.2-2.2a1 1 0 0 1 1-.25 11.4 11.4 0 0 0 3.6.57 1 1 0 0 1 1 1V20a1 1 0 0 1-1 1A17 17 0 0 1 3 4a1 1 0 0 1 1-1h3.5a1 1 0 0 1 1 1c0 1.25.2 2.45.57 3.57a1 1 0 0 1-.25 1z"/></svg>07 5948 2063</li>
        <li><svg viewBox="0 0 24 24"><path d="M7 1h10a2 2 0 0 1 2 2v18a2 2 0 0 1-2 2H7a2 2 0 0 1-2-2V3a2 2 0 0 1 2-2zm0 3v15h10V4z"/></svg>0461 857 239</li>
        <li><svg viewBox="0 0 24 24"><path d="M6 2h10v6H6zM3 9h18a1 1 0 0 1 1 1v9a1 1 0 0 1-1 1H3a1 1 0 0 1-1-1v-9a1 1 0 0 1 1-1zm3 5v2h12v-2z"/></svg>07 5948 2174</li>
      </ul>
      <address class="address">
        3/42 Marlin Crescent<br>
        MARLOW PARK QLD 4125<br>
        <span class="web">www.walshbrody.com</span>
      </address>
    </div>
  </section>

  <section class="card card--back">
    <div class="brand">
      <span class="brand__square"></span>
      <span class="brand__name">WALSH &amp; BRODY PTY LTD.</span>
    </div>
  </section>
</body>
</html>
```